Brisk Fixwell business card

I need business card for my business, I think you have all my details.six months ago I design with you car wrap design. We would like to design both side of the card. On front of card we would like logo , Name and our contact details.
At the back we are looking to mentioned our services.
The name will be:
Farzadullah Korimi
Managing Director
Ph:07843529176
Email:info@brisk-fixwell.com
Web:www.brisk-fixwell.com
So we have our logo, you don’t need to change the logo.
Please see the attachment.
Thanks

Target Market(s)

Home improvement

Industry/Entity Type

Home Improvement

Contact Information for Business Card

Company name: Brisk Fixwell
Name: Farzadullah Korimi
Position: Director
Ph:07843529176
Web: www.brisk-fixwell.com
Add: 42 Larkfield Crescent
Hounslow
TW3 9LB
SECOND PERSON
Nasirudin korimi
Position: Handyman
Ph: 07712 634508
Email: info@brisk-fixwell.com
Add: 18 Wrenmoor Park Lane
Hounslow
TW6 2QJ

```html
<!DOCTYPE html>
<html lang="en">
<head>
<meta charset="utf-8">
<title>Brisk Fixwell – Business Card</title>
<link href="https://fonts.googleapis.com/css2?family=Arimo:wght@400;700&display=swap" rel="stylesheet">
<style>
  :root {
    --navy: #253a80;
    --red: #e11f2d;
    --white: #ffffff;
    --ink: #3c3c3c;
    --grey: #6e6e6e;
    --stage: #2a2a2a;
  }
  * { margin: 0; padding: 0; box-sizing: border-box; }
  html, body { width: 1200px; height: 900px; overflow: hidden; }
  body {
    background: var(--stage);
    font-family: "Arimo", Arial, sans-serif;
    display: flex;
    flex-direction: column;
    align-items: center;
    justify-content: center;
    gap: 56px;
  }
  .card {
    width: 640px;
    height: 366px;
    position: relative;
    overflow: hidden;
    box-shadow: 0 10px 30px rgba(0,0,0,.45);
  }

  /* Back side */
  .card--back { background: var(--navy); color: var(--white); }
  .back-brand {
    position: absolute;
    left: 40px; top: 0; bottom: 0;
    width: 330px;
    display: flex; align-items: center; gap: 16px;
  }
  .back-brand__square { width: 34px; height: 34px; background: var(--red); flex: none; }
  .back-brand__name { font-weight: 700; font-size: 38px; line-height: 1.05; color: var(--white); }
  .services {
    position: absolute;
    left: 392px; top: 58px;
    list-style: none;
  }
  .services li {
    font-size: 14px;
    letter-spacing: .3px;
    line-height: 24.5px;
    display: flex; align-items: center;
  }
  .services li::before {
    content: "";
    width: 9px; height: 9px; border-radius: 50%;
    background: var(--red);
    margin-right: 8px;
  }

  /* Front side */
  .card--front { background: var(--white); }
  .front-brand {
    position: absolute;
    left: 40px; top: 0; bottom: 0; width: 250px;
    display: flex; align-items: center; gap: 12px;
  }
  .front-brand__name { font-weight: 700; font-size: 31px; color: var(--navy); line-height: 1.05; }
  .front-brand__square { width: 26px; height: 26px; background: var(--red); flex: none; }
  .divider {
    position: absolute;
    left: 300px; top: 36px; bottom: 36px; width: 1px;
    background: linear-gradient(to bottom, rgba(0,0,0,0), rgba(0,0,0,.25), rgba(0,0,0,0));
  }
  .contact { position: absolute; left: 334px; top: 78px; color: var(--ink); }
  .contact__name { font-weight: 700; font-size: 21px; color: var(--navy); letter-spacing: .3px; }
  .contact__role { font-size: 14px; color: var(--grey); letter-spacing: .5px; margin-bottom: 14px; }
  .contact__line { display: flex; align-items: center; gap: 8px; font-size: 14.5px; line-height: 23px; }
  .contact__line svg { width: 15px; height: 15px; flex: none; fill: var(--navy); }
  .contact__web .accent { color: var(--navy); }
  .contact__address { margin-top: 12px; font-size: 15px; line-height: 21px; }
</style>
</head>
<body>

<section class="card card--back" aria-label="Card back: services">
  <div class="back-brand">
    <span class="back-brand__square"></span>
    <span class="back-brand__name">Brisk Fixwell</span>
  </div>
  <ul class="services">
    <li>PLUMBING</li>
    <li>CARPENTRY</li>
    <li>PAINTING &amp; DECORATING</li>
    <li>DECKING</li>
    <li>FENCE</li>
    <li>GUTTER</li>
    <li>FLOORING</li>
    <li>PLASTERING</li>
    <li>TILLING</li>
    <li>GARDENING</li>
  </ul>
</section>

<section class="card card--front" aria-label="Card front: contact details">
  <div class="front-brand">
    <span class="front-brand__name">Brisk Fixwell</span>
    <span class="front-brand__square"></span>
  </div>
  <div class="divider"></div>
  <div class="contact">
    <p class="contact__name">FARZADULLAH KORIMI</p>
    <p class="contact__role">DIRECTOR</p>
    <p class="contact__line">
      <svg viewBox="0 0 24 24" aria-hidden="true"><path d="M6.6 10.8a15 15 0 0 0 6.6 6.6l2.2-2.2a1 1 0 0 1 1-.25 11.4 11.4 0 0 0 3.6.57 1 1 0 0 1 1 1V20a1 1 0 0 1-1 1A17 17 0 0 1 3 4a1 1 0 0 1 1-1h3.5a1 1 0 0 1 1 1c0 1.25.2 2.45.57 3.57a1 1 0 0 1-.25 1z"/></svg>
      07843529176
    </p>
    <p class="contact__line">
      <svg viewBox="0 0 24 24" aria-hidden="true"><path d="M2 5h20v14H2z M3.5 6.5 12 13l8.5-6.5" fill="none" stroke="#253a80" stroke-width="2"/></svg>
      info@brisk-fixwell.com
    </p>
    <p class="contact__line contact__web">
      <svg viewBox="0 0 24 24" aria-hidden="true"><circle cx="12" cy="12" r="9.5" fill="none" stroke="#253a80" stroke-width="2"/><path d="M2.5 12h19M12 2.5c3 3 3 16 0 19M12 2.5c-3 3-3 16 0 19" fill="none" stroke="#253a80" stroke-width="1.6"/></svg>
      <span>www.<span class="accent">brisk-fixwell</span>.com</span>
    </p>
    <p class="contact__address">42 Larkfield Crescent<br>Hounslow, TW3 9LB</p>
  </div>
</section>

</body>
</html>
```